A reimagined website for a cross-border tax firm

There are two aspects to this project for Brackwell Tax Consultancy:
1) I need a logo update to accommodate increasing focus and specialization in my business. The byline under the name “Brackwell Tax Consultancy” needs to change:
ORIGINAL: FILING AID FOR CIVIC LEDGER PRACTICES
REVISED: CROSS-BORDER TAX SERVICES • U.S. & CANADA
2) I need a website “refresh” (see current website at www.levyhelpdesk.example) based on this logo – a new vision for a website with greater clarity, focus and organization. It should represent a re-envisioning of the current approach, and not the wholesale abandonment of the style represented there. I need it to be creative, compelling and attention grabbing, but still professional. This should, at a minimum, update any places where the old name/logo is used, but I want the redesign to go beyond this to something more intuitive. I need high quality separate PNG files of the various logo styles for use in various documents, but HTML coding would be a helpful but not necessary addition.

Target Market(s)

People in need of cross-border tax services - Canada and US

Coding

Number of Pages Required

Requirements
Must have
• Greater crispness, sharpness - higher resolution
• A more compelling, organized approach - make the wording and images more accessible to the website user (especially the staff bios, which have scroll bars now)
Nice to have
• Replacement of stock image with a true image of the Halifax skyline
Should not have
• Deviate from colour pattern represented in website logo of blue/orange
• Deviate from existing logo except for word replacement

```html
<!DOCTYPE html>
<html lang="en">
<head>
<meta charset="utf-8">
<title>Brackwell Tax Consultancy</title>
<link href="https://fonts.googleapis.com/css2?family=Lato:wght@300;400;700&display=swap" rel="stylesheet">
<style>
:root{
  --navy:#1b2a5c;
  --blue:#1e73be;
  --link:#3d5a99;
  --orange:#f0892e;
  --red-orange:#e9552a;
  --ink:#222;
  --body:#555;
  --nav:#7d7d7d;
  --rule:#ececec;
  --panel:#f6f6f6;
  --field:#eeeeee;
}
*{box-sizing:border-box;margin:0;padding:0}
html,body{width:1200px;height:1200px;overflow:hidden;background:#fff;font-family:'Lato',sans-serif;color:var(--body)}
.canvas{position:relative;width:1200px;height:1200px}

.sidebar{position:absolute;left:318px;top:44px;width:116px;text-align:center}
.brand{display:flex;flex-direction:column;align-items:center}
.brand-square{width:22px;height:22px;background:var(--navy);margin-bottom:5px}
.brand-name{font-size:6.2px;font-weight:700;color:var(--navy);letter-spacing:.2px;text-transform:uppercase;white-space:nowrap}
.brand-byline{font-size:3.4px;color:var(--navy);margin-top:1px;letter-spacing:.3px;white-space:nowrap}
.nav{list-style:none;margin-top:17px}
.nav li{font-size:8px;font-weight:400;color:var(--nav);height:20.6px;line-height:10px}
.nav li.active{color:var(--link)}
.social{display:flex;justify-content:center;gap:7px;margin-top:7px}
.social span{width:5px;height:5px;border-radius:50%;background:#555}

.main{position:absolute;left:427px;top:0;width:448px;height:1200px;border-right:1px solid #f0f0f0}
.hero{position:absolute;left:0;top:0;width:448px;height:278px;
  background:
    linear-gradient(180deg,rgba(0,0,0,0) 0%,rgba(0,0,0,0) 45%,rgba(28,40,70,.85) 52%,rgba(40,55,90,.9) 66%,rgba(0,0,0,0) 76%),
    radial-gradient(ellipse 60% 12% at 55% 62%,rgba(255,190,120,.55),rgba(255,190,120,0) 70%),
    linear-gradient(180deg,#b6a8c9 0%,#cdb0c6 18%,#e1b3b8 36%,#e8b7ae 46%,#5f6f92 70%,#4e6f98 78%,#6e93bd 90%,#86a9cf 100%)}

.section{position:absolute;left:14px;width:421px}
.section h2{font-size:14.5px;font-weight:700;color:var(--ink);text-transform:uppercase;line-height:1}
.underline{height:2px;margin-top:4px;background:linear-gradient(90deg,var(--red-orange) 0%,var(--orange) 50%,var(--blue) 50.2%,var(--navy) 100%)}
.section p,.section li{font-size:5.25px;line-height:8.3px;color:var(--body)}
.section p{margin-top:8px}
.section p:first-of-type{margin-top:9px}
.section ol,.section ul{margin-top:8px;padding-left:14px}
.section li{margin-bottom:2.7px}
.divider{position:absolute;left:14px;width:421px;height:1px;background:var(--rule)}

.team{display:flex;gap:16px;margin-top:8px}
.member{width:130px;text-align:center}
.portrait{width:130px;height:130px;background:radial-gradient(ellipse 55% 60% at 50% 45%,#6a6a6a 0%,#454545 60%,#2a2a2a 100%)}
.member h3{font-size:7.4px;font-weight:700;color:var(--ink);margin-top:5px;text-transform:uppercase}
.creds{font-size:5px;color:var(--link);height:7px}
.contacts{display:flex;justify-content:center;gap:9px;margin-top:3px;align-items:center}
.dot{width:4px;height:4px;border-radius:50%;background:var(--blue)}
.dot.dark{background:#444}

.map{position:absolute;left:0;top:975px;width:299px;height:187px;
  background:
    radial-gradient(ellipse 35% 30% at 55% 40%,#e6e5df 0%,#e6e5df 60%,rgba(230,229,223,0) 100%),
    radial-gradient(ellipse 40% 28% at 30% 72%,#deddd6 0%,#deddd6 55%,rgba(222,221,214,0) 100%),
    linear-gradient(160deg,#e8e7e2 0%,#e8e7e2 20%,#b7d3e8 38%,#dcdbd4 55%,#b7d3e8 75%,#aecde6 100%)}
.contact{position:absolute;left:299px;top:975px;width:149px;height:187px;background:var(--panel);padding:12px 7px 0}
.contact h2{font-size:14px;font-weight:700;color:var(--ink);text-transform:uppercase;line-height:1}
.contact .underline{width:135px}
.field{width:135px;height:16px;background:var(--field);margin-top:9px;font-size:4.8px;color:#aaa;padding:5px 4px}
.field.message{height:42px}
.send{width:45px;height:14px;background:var(--navy);color:#fff;font-size:4.8px;font-weight:700;display:flex;align-items:center;justify-content:center;margin-top:8px;text-transform:uppercase}

.footer{position:absolute;left:0;top:1173px;width:448px;text-align:center;font-size:5px;line-height:8px;color:var(--body)}
.to-top{position:absolute;left:425px;top:1178px;width:18px;height:17px;background:#9a9a9a;display:flex;align-items:center;justify-content:center}
</style>
</head>
<body>
<div class="canvas">
  <aside class="sidebar">
    <div class="brand">
      <div class="brand-square"></div>
      <div class="brand-name">Brackwell Tax Consultancy</div>
      <div class="brand-byline">CROSS-BORDER TAX SERVICES • U.S. &amp; CANADA</div>
    </div>
    <ul class="nav">
      <li class="active">Home</li>
      <li>For Individuals</li>
      <li>For Firms</li>
      <li>Our Team</li>
      <li>Contact Us</li>
      <li>Payment</li>
    </ul>
    <div class="social"><span></span><span></span><span></span><span></span><span></span></div>
  </aside>

  <main class="main">
    <div class="hero" role="img" aria-label="City skyline across the harbour at dusk, pink sky over lit towers and calm blue water"></div>

    <section class="section" style="top:299px">
      <h2>For Individuals</h2>
      <div class="underline"></div>
      <p>We are firm devoted to helping individuals and businesses determine, comply with and minimize/optimize their Canadian and U.S. tax obligations. Let's take a moment to unpack that sentence.</p>
      <p>There are three elements to what we can do for you:</p>
      <ol>
        <li>We can help you determine the Canadian and/or U.S. tax implications of your current situation and your compliance (i.e. tax filing and administration) obligations;</li>
        <li>We can help you determine if there is a better way to structure your affairs, so as to minimize/reduce your tax bill and/or your compliance burden;</li>
        <li>We can prepare tax returns and other filings for submission to the federal and state tax authorities in the U.S. or the Northern Revenue Office in Canada.</li>
      </ol>
      <p>We try to complement, not compete with, other Canadian accounting firms. As a result, we restrict our work to situations that call for our cross-border expertise. If you have ordinary Canadian tax obligations which do not involve cross-border complications, we'll refer you to another accounting firm. If you already have a Canadian accountant, we would be happy to work with that individual while handling/assisting with only the international aspect of your affairs (such as your U.S. tax filings).</p>
      <p>What that means is that while we will accept any U.S. oriented engagement, we will only accept Canadian tax advisory and compliance assignments where they involve cross-border or international complications. But don't hesitate to call – if we aren't right for you, we can certainly refer you to other competent advisors.</p>
    </section>
    <div class="divider" style="top:478px"></div>

    <section class="section" style="top:503px">
      <h2>For Public Accounting Firms</h2>
      <div class="underline"></div>
      <p>We provide a range of services to Canadian public accounting firms (PAFs) to assist them in serving their clients.</p>
      <p>In general, our PAF clients are small firms which are not large enough to have their own internal tax specialists. We can assist you by providing you with access to tax support on an "as-needed" basis. We can perform research and assist with unusual or complex compliance. We can also help you with tax planning for your clients – both by developing plans and by overseeing their execution. Common examples of projects we oversee include incorporating businesses, reorganizing the share capital of corporations, the creation and use of various types of trusts and the transfer of assets from individuals to companies or from one corporation to another.</p>
      <p>For PAFs with their own tax staff, we can provide brainstorming, review and second opinion services in respect of work performed internally.</p>
      <p>Even mid-sized firms with tax specialists often draw the line when cross-border tax considerations become involved. The majority of our referrals relate to our specialization in cross-border/international taxation.</p>
      <p>Working with Brackwell Tax Consultancy offers PAFs the following benefits:</p>
      <ul>
        <li>Risk mitigation – we are able to significantly lower your risk in areas of tax in which you rarely or never practice;</li>
        <li>Cost reduction – for most small to mid-sized firms, we are significantly cheaper on an annual basis when compared to having in-house tax specialists;</li>
        <li>Non-competition – because we do not offer the year-end and tax compliance services of a typical PAF, we do not present a competitive threat (we won't steal your clients);</li>
        <li>Hourly rate alignment – our staff's hourly rates are aligned with those of our PAF clients.</li>
      </ul>
    </section>
    <div class="divider" style="top:714px"></div>

    <section class="section" style="top:737px">
      <h2>Our Team</h2>
      <div class="underline"></div>
      <div class="team">
        <div class="member">
          <div class="portrait" role="img" aria-label="Studio portrait of team member in dark suit on grey backdrop"></div>
          <h3>Martin R. Ellory</h3>
          <div class="creds">CPA, CGA, EA</div>
          <div class="contacts">
            <svg width="6" height="4" viewBox="0 0 6 4"><rect width="6" height="4" fill="#777"/><path d="M0 0l3 2 3-2" stroke="#fff" stroke-width=".5" fill="none"/></svg>
            <span class="dot dark"></span><span class="dot"></span><span class="dot"></span>
          </div>
        </div>
        <div class="member">
          <div class="portrait" role="img" aria-label="Studio portrait of team member in navy suit on grey backdrop"></div>
          <h3>Gavin Thorley</h3>
          <div class="creds">CPA, CA</div>
          <div class="contacts">
            <svg width="6" height="4" viewBox="0 0 6 4"><rect width="6" height="4" fill="#777"/><path d="M0 0l3 2 3-2" stroke="#fff" stroke-width=".5" fill="none"/></svg>
            <span class="dot dark"></span><span class="dot"></span><span class="dot"></span>
          </div>
        </div>
        <div class="member">
          <div class="portrait" role="img" aria-label="Studio portrait of team member in white blouse on grey backdrop"></div>
          <h3>Clara J. Ellory</h3>
          <div class="creds"></div>
          <div class="contacts">
            <svg width="6" height="4" viewBox="0 0 6 4"><rect width="6" height="4" fill="#777"/><path d="M0 0l3 2 3-2" stroke="#fff" stroke-width=".5" fill="none"/></svg>
            <span class="dot dark"></span><span class="dot"></span><span class="dot"></span>
          </div>
        </div>
      </div>
    </section>
    <div class="divider" style="top:951px"></div>

    <div class="map" role="img" aria-label="Regional coastline map with two office location pins"></div>
    <div class="contact">
      <h2>Get In Touch</h2>
      <div class="underline"></div>
      <div class="field">Full Name</div>
      <div class="field">Phone Number</div>
      <div class="field">Email Address</div>
      <div class="field message">Your Message</div>
      <div class="send">Send Mail</div>
    </div>

    <footer class="footer">© Copyright 2017 Brackwell Tax Consultancy<br>All Rights Reserved</footer>
    <div class="to-top"><svg width="7" height="5" viewBox="0 0 7 5"><path d="M.5 4.5l3-3 3 3" stroke="#fff" stroke-width="1" fill="none"/></svg></div>
  </main>
</div>
</body>
</html>
```